Tidewell Marketing company is looking for a web page design

Your projects should contain:

1. Header: Logo provided by us.
2. Top nav bar: offer, about us, experience, contact.
3. “Choose language” button.
4. Main section: panoramic picture (static, professional, modern).
5. Below section: 3 blocks (image+title+description), which represent our 3 main activities (titles):
• Market Research,
• Marketing Plans,
• Marketing Project.
6. ‘Contact us’ form – Message (text: “Write your message and give us details about your company and activities”), Email, SEND).
7. Page footer: (4 section: Contact, Social Media, Blog, Partners).
Updates

Hello!

I uploaded new file 'general_look', which is our idea how the page should generally look like.

BUT! it doesn't mean that your projects should look exactly like this project e.g.:
* titles Market Research, Marketing Plans, Marketing Project can be above these: Image 1,2,3.
* everything doesn't have to be in square and rectangle shape. You can try to manipulate with blocks and can add elipse elemnts or something similar.

We will appreciate your innovative ideas. Just wanted to give you general plan of the site and ilustrate all elements that we require.

Best Regards,
Benedek

IMPORTENT

Please remember that the main picture should be panoramic. Please do not close it in frame.

Target Market(s)

Small and middle sized companies, which would like to export their goods and services abroad and are interested in raising funds from Northgate Trade Council to expand their activities. These are rather industrial companies with low level of innovativeness. Our mission is to build image of the client’s company and increase awareness of their products to improve their competitiveness and innovativeness.

Industry/Entity Type

It Company

Requirements
Must have
• 1. Create designs of main page and subpage.
2. Subpage: Logo, Header, language button, place for article, navigation menu on the right side - below it “contact us” button , footer on the bottom. (In this section we are looking mainly for the design of the header and navigation menu).
3. The whole design should be a series of horizontal blocks.
4. Your projects should be associated with features such as: Reliability, Security, Professionalism, Openness, Uniqueness.
5. The design should be simple, fresh, readable, easy to use and should create a feeling of high quality services.
6. Possibility to change the panoramic picture (separate layer in a graphic file).
7. All pictures and blocks should be static, no movements.
8. Style of the page should be compliant with the logo design, font: Swiss.
9. Designs that we like: http://www.fernvale-studio.pl/, http://www.plumquarry.com/.
Should not have
• There shouldn’t be any distractions and not matching parts (whole design should be compact and easy to interpret and remember).

```html
<!DOCTYPE html>
<html lang="en">
<head>
<meta charset="utf-8">
<title>Tidewell Marketing — your passport to foreign markets</title>
<link rel="stylesheet" href="https://fonts.googleapis.com/css2?family=Arimo:wght@400;700&display=swap">
<style>
  :root {
    --stage-inner: #8d969c;
    --stage-outer: #3b4145;
    --frame: #a6aeb4;
    --frame-light: #f4f5f6;
    --nav-strip: #d6dadd;
    --ink: #3a3f43;
    --ink-soft: #686e72;
    --welcome: #7c858b;
    --accent: #12b6ec;
    --green: #8cc63f;
    --orange: #f9a51a;
    --white: #ffffff;
    --footer-note: #b7bec2;
    --logo-blue: #1b4f7a;
  }
  * { box-sizing: border-box; margin: 0; padding: 0; }
  html, body { width: 1200px; height: 951px; overflow: hidden; }
  body {
    position: relative;
    font-family: "Arimo", Helvetica, Arial, sans-serif;
    background: radial-gradient(ellipse at 50% 45%, var(--stage-inner) 0%, #6b7378 55%, var(--stage-outer) 100%);
    color: var(--ink);
  }
  .page {
    position: absolute; left: 164px; top: 60px; width: 877px; height: 848px;
    border-radius: 18px;
    background: linear-gradient(160deg, var(--frame-light) 0%, #e3e6e8 22%, var(--frame) 45%, var(--frame) 100%);
  }
  .feedback-tab {
    position: absolute; left: 1036px; top: 613px; width: 28px; height: 140px;
    background: var(--frame); border-radius: 0 10px 10px 0;
    display: flex; align-items: center; justify-content: center;
  }
  .feedback-tab span {
    transform: rotate(-90deg); color: var(--white); font-size: 17px; letter-spacing: 1px; white-space: nowrap;
  }
  .language-button {
    position: absolute; left: 902px; top: 81px; width: 117px; height: 29px;
    border-radius: 8px; background: var(--accent); color: var(--white);
    font-size: 13px; display: flex; align-items: center; gap: 6px; padding-left: 10px;
  }
  .brand { position: absolute; left: 196px; top: 118px; }
  .brand-name { display: flex; align-items: center; gap: 8px; font-size: 29px; color: var(--logo-blue); letter-spacing: -0.5px; line-height: 1; }
  .brand-mark { width: 42px; height: 42px; border-radius: 50%; background: var(--logo-blue); }
  .brand-tagline { position: absolute; left: 96px; top: 32px; font-size: 10px; color: var(--logo-blue); white-space: nowrap; }
  .nav-strip {
    position: absolute; left: 492px; top: 128px; width: 539px; height: 32px; background: var(--nav-strip);
  }
  .nav { display: flex; align-items: center; height: 32px; font-size: 11px; }
  .nav a { color: #222; text-decoration: none; padding: 0 9px; border-left: 1px solid #fff; line-height: 18px; }
  .nav a.is-active { background: #1e1e1e; color: var(--white); line-height: 30px; border: 0; padding: 0 6px; margin-left: 1px; }
  .nav a.is-active + a { border-left: 0; }
  .search { position: absolute; right: 30px; top: 6px; width: 172px; height: 20px; background: var(--white); border: 1px solid #7b8287; }
  .search-icon { position: absolute; right: 8px; top: 6px; }
  .content {
    position: absolute; left: 174px; top: 183px; width: 857px; height: 607px;
    background: var(--white); border-radius: 0 0 8px 8px;
  }
  .hero {
    position: absolute; left: 0; top: 0; width: 857px; height: 288px;
    background: linear-gradient(90deg, #ffffff 0%, #ffffff 32%, #e9ecee 45%, #c9ced2 70%, #dde1e3 100%);
  }
  .hero-title { position: absolute; left: 93px; top: 126px; font-size: 62px; color: var(--accent); line-height: 1; letter-spacing: 0.5px; }
  .hero-sub { position: absolute; left: 163px; top: 193px; font-size: 39px; color: #5e6366; line-height: 1; letter-spacing: 0.3px; }
  .welcome { position: absolute; left: 95px; top: 337px; width: 670px; }
  .welcome h1 {
    display: inline-block; font-weight: 400; font-size: 30px; color: var(--welcome); line-height: 1;
    padding-right: 4px; padding-bottom: 3px; border-bottom: 1px solid #b5bbbf; letter-spacing: -0.5px;
  }
  .welcome h1 small { font-size: 22px; letter-spacing: 0; }
  .welcome p { margin-top: 6px; font-size: 12px; line-height: 13px; color: #444; text-align: justify; }
  .service {
    position: absolute; top: 648px; width: 220px; height: 164px; background: var(--white); padding: 3px 5px 6px;
  }
  .service-body { position: relative; width: 100%; height: 100%; color: var(--white); }
  .service--research .service-body { background: var(--accent); }
  .service--plans .service-body { background: var(--green); }
  .service--project .service-body { background: var(--orange); }
  .service-image { position: absolute; left: 4px; top: 4px; right: 4px; height: 53px; border: 3px solid #1d1d1d; }
  .service h2 { position: absolute; left: 14px; top: 62px; font-weight: 400; font-size: 22px; line-height: 1; }
  .service h3 { position: absolute; left: 15px; top: 84px; font-weight: 400; font-size: 13px; line-height: 1; }
  .service p {
    position: absolute; left: 75px; top: 90px; width: 120px; font-size: 8px; line-height: 9.3px;
    border-left: 1px solid var(--white); padding-left: 4px; height: 42px;
  }
  .read-more { position: absolute; right: 12px; bottom: 9px; font-size: 8px; color: var(--white); text-decoration: none; }
  .footer-links { position: absolute; left: 0; width: 1200px; top: 839px; display: flex; justify-content: center; font-size: 17px; }
  .footer-links a { color: var(--white); text-decoration: none; padding: 0 9px; border-left: 2px solid #e6e9eb; line-height: 22px; }
  .footer-links a:first-child { border-left: 0; }
  .share { position: absolute; left: 522px; top: 867px; display: flex; align-items: center; height: 32px; gap: 8px; }
  .share-label { color: var(--white); font-size: 13px; text-decoration: underline; padding-right: 10px; border-right: 2px solid #e6e9eb; line-height: 32px; }
  .share-dot { width: 16px; height: 16px; border-radius: 50%; background: var(--white); }
  .copyright { position: absolute; left: 0; width: 1200px; top: 922px; text-align: center; font-size: 11px; color: var(--footer-note); letter-spacing: 0.3px; }
</style>
</head>
<body>
  <div class="page"></div>
  <div class="feedback-tab"><span>feedback</span></div>

  <header>
    <a class="language-button" href="#">
      <svg width="20" height="16" viewBox="0 0 20 16" aria-hidden="true"><circle cx="8" cy="8" r="7" fill="#fff"/><path d="M16 4 q3 4 0 8" stroke="#fff" stroke-width="1.3" fill="none"/></svg>
      language
      <svg width="12" height="13" viewBox="0 0 12 13" aria-hidden="true"><path d="M1 0 L12 6.5 L1 13 Z" fill="#fff"/></svg>
    </a>
    <div class="brand">
      <div class="brand-name"><span class="brand-mark"></span>tidewell marketing</div>
      <div class="brand-tagline">your passport to foreign markets</div>
    </div>
    <div class="nav-strip">
      <nav class="nav">
        <a class="is-active" href="#">Offer</a>
        <a href="#">About us</a>
        <a href="#">Experience</a>
      </nav>
      <div class="search"></div>
      <svg class="search-icon" width="16" height="17" viewBox="0 0 16 17" aria-hidden="true"><circle cx="9.5" cy="6.5" r="5" stroke="#222" stroke-width="2" fill="none"/><path d="M6 10 L1 16" stroke="#222" stroke-width="2.4"/></svg>
    </div>
  </header>

  <main class="content">
    <section class="hero" role="img" aria-label="Panoramic photo: magnifying glass resting on a printed line chart, in soft grey tones">
      <div class="hero-title">your passport</div>
      <div class="hero-sub">to foreign markets</div>
    </section>

    <section class="welcome">
      <h1>WELCOME<small>tidewell marketing</small></h1>
      <p>Managers need information in order to introduce products and services that create value in the mind of the customer.Managers need information in order to introduce products and services that create value in the mind of the customer. Managers need information in order to introduce products and services that create value in the mind of the customer.</p>
    </section>
  </main>

  <article class="service service--research" style="left:264px">
    <div class="service-body">
      <div class="service-image" role="img" aria-label="Photo of a magnifying glass over a chart" style="background:linear-gradient(90deg,#d9dcde,#f2f3f4 60%,#c4c8cb)"></div>
      <h2>Market</h2><h3>Research</h3>
      <p>Managers need information in order to introduce products and services that create value in the mind of the customer.</p>
      <a class="read-more" href="#">read more</a>
    </div>
  </article>
  <article class="service service--plans" style="left:492px">
    <div class="service-body">
      <div class="service-image" role="img" aria-label="Photo of a business person touching a screen of growth and market keywords" style="background:linear-gradient(90deg,#1e3f5a,#2f6a8c 55%,#1a2e40)"></div>
      <h2>Marketing</h2><h3>Plans</h3>
      <p>Managers need information in order to introduce products and services that create value in the mind of the customer.</p>
      <a class="read-more" href="#">read more</a>
    </div>
  </article>
  <article class="service service--project" style="left:724px">
    <div class="service-body">
      <div class="service-image" role="img" aria-label="Photo of a business handshake" style="background:linear-gradient(90deg,#5a5f63,#c9c5c0 50%,#4a4f53)"></div>
      <h2>Marketing</h2><h3>Project</h3>
      <p>Managers need information in order to introduce products and services that create value in the mind of the customer.</p>
      <a class="read-more" href="#">read more</a>
    </div>
  </article>

  <footer>
    <nav class="footer-links">
      <a href="#">Contact</a><a href="#">Social Media</a><a href="#">Blog</a><a href="#">Partners</a>
    </nav>
    <div class="share">
      <span class="share-label">Share</span>
      <span class="share-dot"></span>
      <span class="share-dot"></span>
      <svg width="24" height="16" viewBox="0 0 24 16" aria-label="Email"><rect width="24" height="16" fill="#fff"/><path d="M0 0 L12 9 L24 0" stroke="#a6aeb4" stroke-width="2" fill="none"/></svg>
      <svg width="20" height="22" viewBox="0 0 20 22" aria-label="Print"><rect x="4" y="0" width="12" height="6" fill="#fff"/><rect x="0" y="7" width="20" height="9" rx="2" fill="#fff"/><rect x="4" y="14" width="12" height="8" fill="#fff" stroke="#a6aeb4"/></svg>
    </div>
    <div class="copyright">© 2012 Copyright XXXXXXXXXX. All rights reserved.</div>
  </footer>
</body>
</html>
```